依頼詳細
タワーマンションの理事長にチラシを配布しようと思っています。そのチラシデザイン制作をお願いします。見る人が思わず参加したくなるようなインパクトのあるデザインをお願いします。
記載項目
社名:株式会社MN建築設計/電話:06-4827-3956/URL:http://mn-kenchiku.co.jp
サイズ
A4
ページ数
両面
希望イメージ
シンプル 複雑
単色 カラフル
暗い 明るい
日常 高級
遊び心 厳粛
未来的 伝統的
女性的 男性的

弊社のイメージカラーに合っていたこと、内容が見やすくて分かりやすかった為

このたびは短い期間でありながらもご参加いただきありがとうございました。
皆様の提案は全て良かったので選定に苦慮いたしました。今回選定されなかったご提案者様は残念な結果となりましたが、今後もご提案をお願いするときには是非参加くださいますようお願い申し上げます。

```html
<!DOCTYPE html>
<html lang="ja">
<head>
<meta charset="UTF-8">
<title>タワーマンション管理組合 交流会</title>
<link href="https://fonts.googleapis.com/css2?family=Noto+Sans+JP:wght@400;500;700;900&display=swap" rel="stylesheet">
<style>
:root{
  --navy:#1d2a6e;
  --purple:#4b2a8c;
  --cyan:#1e9fdc;
  --sky:#a9d6f2;
  --magenta:#d6257a;
  --yellow:#ffe34d;
  --ink:#1b1d3a;
  --white:#ffffff;
  --pale:#eef4fb;
}
*{margin:0;padding:0;box-sizing:border-box}
html,body{width:851px;height:1200px;overflow:hidden;background:var(--white)}
body{font-family:"Noto Sans JP",sans-serif;color:var(--ink);position:relative}
.hero-visual{position:absolute;left:0;top:0;width:851px;height:810px;
  background:linear-gradient(160deg,#e8f5ff 0%,#9fd0f0 35%,#3f8fd0 70%,#2a5ea8 100%)}
.top-band{position:absolute;left:0;top:0;width:851px;height:70px;background:var(--navy)}
.top-band .org{position:absolute;left:95px;top:14px;padding:6px 40px;border:2px solid var(--white);border-radius:30px;color:var(--white);font-weight:700;font-size:26px;letter-spacing:.08em}
.title{position:absolute;left:40px;top:88px;font-weight:900;font-size:178px;line-height:1;color:var(--navy);letter-spacing:.02em;-webkit-text-stroke:6px var(--white);paint-order:stroke fill}
.theme{position:absolute;left:575px;top:112px;width:245px;padding:14px 10px;background:var(--white);border:3px solid var(--navy);text-align:center;font-weight:900;color:var(--navy);font-size:26px;line-height:1.35}
.theme em{font-style:normal;color:var(--magenta);font-size:40px;background:linear-gradient(transparent 60%,var(--yellow) 60%)}
.slogan{position:absolute;left:30px;top:318px;width:790px;height:62px;background:var(--purple);color:var(--white);font-weight:900;font-size:40px;line-height:62px;padding-left:70px;letter-spacing:.03em}
.slogan em{font-style:normal;color:var(--yellow)}
.bubble{position:absolute;background:var(--white);border:3px solid var(--navy);border-radius:14px;font-weight:900;color:var(--navy);padding:10px 18px;line-height:1.25}
.bubble::after{content:"";position:absolute;bottom:-16px;width:0;height:0;border-left:12px solid transparent;border-right:12px solid transparent;border-top:16px solid var(--navy)}
.bubble.l::after{left:40px}.bubble.r::after{right:40px}
.bubble em{font-style:normal;color:var(--cyan);font-size:1.6em}
.bubble .hot{color:var(--magenta)}
.b1{left:30px;top:420px;font-size:26px}
.b2{left:585px;top:410px;font-size:30px}
.b3{left:250px;top:530px;font-size:36px}
.b4{left:580px;top:610px;font-size:30px}
.b5{left:25px;top:660px;font-size:30px}
.notice{position:absolute;left:30px;top:826px;width:480px;padding:6px 12px;border:2px solid var(--navy);background:var(--pale);font-size:11.5px;line-height:1.45}
.notice h3{color:var(--magenta);font-size:14px;font-weight:900}
.info{position:absolute;left:30px;top:920px;width:490px}
.row{display:flex;align-items:center;height:44px;margin-bottom:7px}
.row dt{flex:none;width:98px;height:36px;background:var(--navy);color:var(--white);font-weight:700;font-size:19px;display:flex;align-items:center;justify-content:center;letter-spacing:.3em;margin-right:14px}
.row dt.tight{letter-spacing:.02em;font-size:18px}
.row dd{font-weight:900;color:var(--navy);font-size:21px;line-height:1.1}
.row .big{font-size:40px;color:var(--magenta)}
.row .sm{font-size:14px;font-weight:500}
.row .addr{display:block;font-size:10.5px;font-weight:400;color:var(--ink);margin-top:3px}
.row .red{color:var(--magenta)}
.program{position:absolute;left:540px;top:826px;width:285px;height:296px;border:3px solid var(--navy);background:var(--white);padding:10px 14px}
.program h2{background:var(--navy);color:var(--white);font-size:21px;font-weight:900;text-align:center;letter-spacing:.3em;padding:4px 0;margin-bottom:10px}
.part{margin-bottom:10px}
.part .tag{display:inline-block;background:var(--purple);color:var(--white);font-size:12px;font-weight:700;padding:1px 7px;margin-right:6px}
.part .name{font-weight:900;color:var(--navy);font-size:16px}
.part .name small{font-size:11px}
.part p{font-size:11px;line-height:1.4;margin:4px 0}
.part .time{display:block;font-weight:900;font-size:22px;color:var(--magenta)}
.footer{position:absolute;left:0;top:1142px;width:851px;height:58px;background:var(--navy);color:var(--white);display:flex;align-items:center;padding:0 30px;justify-content:space-between}
.footer .host{font-weight:700;font-size:20px}
.footer .contact{font-size:14px;display:flex;align-items:center;gap:10px}
.footer .dot{width:30px;height:30px;border-radius:50%;background:var(--white)}
</style>
</head>
<body>
<div class="hero-visual" role="img" aria-label="青空にそびえるタワーマンション群の写真"></div>
<header class="top-band"><p class="org">タワーマンション管理組合</p></header>
<h1 class="title">交流会</h1>
<p class="theme">分譲マンションの<br><em>未来</em>を考える</p>
<p class="slogan">管理組合の<em>自立</em>を目指す!</p>

<p class="bubble b1 l">他のタワーマンションは <em>どう?</em></p>
<p class="bubble b2 r"><span class="hot">修繕費</span>が<br>高くない??</p>
<p class="bubble b3 l"><span class="hot">管理費</span>の値上げ??</p>
<p class="bubble b4 r"><span class="hot">民泊問題</span>は<br>どうする?</p>
<p class="bubble b5 l"><span class="hot">理事</span>のなり手<br>がないがどうする?</p>

<section class="notice">
  <h3>新型コロナウイルス対策について</h3>
  <p>交流会では「新型コロナウイルス」の感染予防対策を実施しております。アルコール消毒・マスク着用・検温にご協力ください。体調不良の方はご参加をお控えください。</p>
</section>

<dl class="info">
  <div class="row"><dt>日時</dt><dd><span class="sm">2022</span> <span class="big">7.31</span>(日) 10:00〜12:00</dd></div>
  <div class="row"><dt>定員</dt><dd><span class="sm">先着</span><span class="red">15</span>名様</dd></div>
  <div class="row"><dt>会場</dt><dd>ミナトタワーレジデンス天王寺<span class="addr">大阪府大阪市天王寺区上本町9丁目2番10号</span></dd></div>
  <div class="row"><dt class="tight">申込締切</dt><dd><span class="sm">2022</span> <span class="big">7.19</span>(火)</dd></div>
</dl>

<section class="program">
  <h2>開催内容</h2>
  <div class="part">
    <span class="tag">第1部</span><span class="name">意見交流会<small>(全員参加型)</small></span>
    <p>参加者の方々で、課題を共有し、解決策を探ります。</p>
    <span class="time">10:00〜10:50</span>
  </div>
  <div class="part">
    <span class="tag">第2部</span><span class="name">修繕工事の進め方と考え方</span>
    <p>講師 <b style="font-size:17px;color:var(--navy)">三森 健</b>(一級建築士)</p>
    <span class="time">11:00〜12:00</span>
  </div>
</section>

<footer class="footer">
  <p class="host">主催:マンション管理組合交流会</p>
  <p class="contact">お問い合わせ・お申し込みは、裏面をご覧ください。<span class="dot"></span></p>
</footer>
</body>
</html>
```